Mexican Tacos Food Truck Menu

Attached is the food truck logo. Need a menu to be place next to the window. Must contain:
- logo in the header (left or centered)
- Grouping elements: Dessert, drinks, Apps, etc.
- Group elements.
- main descrition (these are examples) Spaguetti, Pastor, etc
- Notes. Under main item for ingrediens, GF, dairy, etc.
- Price. Should be fairly visible and justify to the right
No prodiving target size but the I the design should accomodate at least two Group columns. I should be able to add or remove as needed.
Since the food truck is blue I think menu should be white based unless you have other options. I will update blue code

```html
<!DOCTYPE html>
<html lang="en">
<head>
<meta charset="utf-8">
<title>Taquería Azul – Menu</title>
<link rel="stylesheet" href="https://fonts.googleapis.com/css2?family=Anton&family=Montserrat:wght@500;600;800&family=Alegreya:wght@700&display=swap">
<style>
  :root {
    --navy: #1c2f7a;
    --red: #e34436;
    --red-deep: #c83d3f;
    --ink: #0d0d0d;
    --paper: #ffffff;
  }
  * { box-sizing: border-box; margin: 0; padding: 0; }
  html, body { width: 848px; height: 1200px; overflow: hidden; background: var(--paper); }
  .menu-board {
    position: relative;
    width: 848px;
    height: 1200px;
    overflow: hidden;
    background: var(--paper);
    font-family: "Montserrat", sans-serif;
    color: var(--ink);
  }
  .header-art { position: absolute; left: 0; top: 0; width: 848px; height: 440px; }
  .footer-art { position: absolute; left: 0; bottom: 0; width: 848px; height: 110px; }

  .brand {
    position: absolute;
    left: 35px; top: 35px;
    width: 170px; height: 170px;
    border-radius: 50%;
    background: var(--paper);
    border: 6px solid var(--red);
    display: flex; align-items: center; justify-content: center;
    text-align: center;
  }
  .brand-name {
    font-weight: 800;
    font-size: 22px;
    line-height: 1.1;
    color: var(--navy);
  }

  .page-title {
    position: absolute;
    left: 249px; top: 168px;
    font-family: "Anton", sans-serif;
    font-weight: 400;
    font-size: 164px;
    line-height: 1;
    letter-spacing: 9px;
    color: var(--ink);
  }

  .divider {
    position: absolute;
    left: 423px; top: 468px;
    width: 3px; height: 611px;
    background: var(--red);
  }

  .menu-group { position: absolute; width: 352px; }
  .group-tacos    { left: 38px;  top: 467px; }
  .group-desserts { left: 462px; top: 467px; }
  .group-drinks   { left: 38px;  top: 838px; }
  .group-adds     { left: 462px; top: 838px; }

  .group-title {
    height: 52px;
    background: var(--navy);
    color: var(--red);
    font-weight: 800;
    font-size: 28px;
    line-height: 52px;
    text-align: center;
    letter-spacing: 0.5px;
    margin-bottom: 20px;
  }

  .menu-item { height: 58px; }
  .item-line {
    width: 322px;
    display: grid;
    grid-template-columns: auto 1fr 73px;
    align-items: baseline;
    column-gap: 5px;
  }
  .item-name { font-weight: 500; font-size: 25px; line-height: 34px; white-space: nowrap; }
  .item-leader {
    border-bottom: 3px dotted var(--ink);
    transform: translateY(-6px);
    margin-right: 5px;
  }
  .item-price { font-weight: 600; font-size: 25px; line-height: 34px; white-space: nowrap; }
  .item-note {
    font-family: "Alegreya", serif;
    font-weight: 700;
    font-size: 11.7px;
    line-height: 15px;
    white-space: nowrap;
  }
  .leader-wide { margin-left: 30px; }
  .leader-gap { margin-left: 6px; }
</style>
</head>
<body>
<main class="menu-board">

  <svg class="header-art" viewBox="0 0 848 440" role="img" aria-label="Bold red wave over navy with a flowing yellow contour-line pattern">
    <rect x="0" y="0" width="848" height="440" fill="var(--navy)"/>
    <path fill="var(--red)" d="M307,0 C292,40 300,72 262,95 C214,122 205,160 205,232 C205,272 190,292 120,302 C62,310 40,342 20,380 L0,402 L0,440 L848,440 L848,312 C802,302 782,272 800,242 C830,202 822,170 792,150 C742,120 712,60 700,0 Z"/>
    <path fill="var(--paper)" d="M0,410 C40,396 80,386 120,400 C160,414 200,390 240,396 C270,400 266,410 300,406 C340,401 380,396 420,406 C460,416 490,432 520,421 C560,408 600,391 650,396 C690,400 720,386 760,381 C800,378 822,396 848,400 L848,440 L0,440 Z"/>
  </svg>

  <div class="brand">
    <span class="brand-name">Taquería<br>Azul</span>
  </div>

  <h1 class="page-title">MENU</h1>

  <div class="divider"></div>

  <section class="menu-group group-tacos">
    <h2 class="group-title">TACOS</h2>
    <div class="menu-item">
      <div class="item-line"><span class="item-name">Pastor</span><span class="item-leader"></span><span class="item-price">$3.00</span></div>
      <p class="item-note">(marinated pork, onion, cilantro and pineapple in CORN tortilla)</p>
    </div>
    <div class="menu-item">
      <div class="item-line"><span class="item-name">Dirty Pastor</span><span class="item-leader"></span><span class="item-price">$3.50</span></div>
      <p class="item-note">(marinated pork, cheese, onion, cilantro and pineapple in CORN tortilla)</p>
    </div>
    <div class="menu-item">
      <div class="item-line"><span class="item-name">1/2 Gringa</span><span class="item-leader"></span><span class="item-price">$4.00</span></div>
      <p class="item-note">(marinated pork, cheese, onion, cilantro and pineapple in CORN tortilla)</p>
    </div>
    <div class="menu-item">
      <div class="item-line"><span class="item-name">Volcano</span><span class="item-leader"></span><span class="item-price">$3.50</span></div>
      <p class="item-note">(marinated pork, cheese, onion, cilantro and pineapple in CORN tortilla)</p>
    </div>
  </section>

  <section class="menu-group group-desserts">
    <h2 class="group-title">DESSERTS</h2>
    <div class="menu-item">
      <div class="item-line"><span class="item-name">Flan</span><span class="item-leader leader-wide"></span><span class="item-price">$3.00</span></div>
      <p class="item-note">(Eggs, dairy, high calories)</p>
    </div>
  </section>

  <section class="menu-group group-drinks">
    <h2 class="group-title">DRINKS</h2>
    <div class="menu-item">
      <div class="item-line"><span class="item-name">Horchata</span><span class="item-leader"></span><span class="item-price">$2.50</span></div>
      <p class="item-note">(diary, good for pastor tacos and better if you went for hot salsa)</p>
    </div>
    <div class="menu-item">
      <div class="item-line"><span class="item-name">Jamaica</span><span class="item-leader leader-gap"></span><span class="item-price">$2.50</span></div>
      <p class="item-note">&nbsp;(hibiscus, very refreshing)</p>
    </div>
    <div class="menu-item">
      <div class="item-line"><span class="item-name">Sodas</span><span class="item-leader leader-gap"></span><span class="item-price">$1.50</span></div>
    </div>
  </section>

  <section class="menu-group group-adds">
    <h2 class="group-title">Adds</h2>
    <div class="menu-item">
      <div class="item-line"><span class="item-name">Guacamole</span><span class="item-leader leader-gap"></span><span class="item-price">$0.50</span></div>
      <p class="item-note">(hot or mild)&nbsp; (avocado, cilantro, onion, tomato)</p>
    </div>
    <div class="menu-item">
      <div class="item-line"><span class="item-name">Pico de gallo</span><span class="item-leader"></span><span class="item-price">$0.75</span></div>
      <p class="item-note">&nbsp;(avocado, cilantro, onion, tomato)</p>
    </div>
  </section>

  <svg class="footer-art" viewBox="0 0 848 110" role="img" aria-label="Red wave band with a navy speckle texture">
    <defs>
      <linearGradient id="footer-tone" x1="0" y1="0" x2="0" y2="1">
        <stop offset="0" stop-color="var(--red)"/>
        <stop offset="1" stop-color="var(--red-deep)"/>
      </linearGradient>
    </defs>
    <path fill="url(#footer-tone)" d="M0,30 C30,20 60,40 90,28 C120,16 140,0 170,6 C200,12 220,30 250,26 C280,22 300,40 330,36 C370,32 380,22 395,40 C410,50 420,28 450,22 C480,16 520,30 560,22 C600,14 620,6 650,14 C680,22 700,40 730,30 C760,20 800,10 848,22 L848,110 L0,110 Z"/>
  </svg>

</main>
</body>
</html>
```